Hope KLN Disease (Non-Profit) Tri-Fold Brochure Design

We have put together the content for a brochure that we will distribute to doctors, researchers and patients about our non-profit. We would like the design of the brochure to look more professional and have nice aesthetics. It needs to incorporate all of the content in the attached Word file. We will have printed once we have a finished design.

Target Market(s)

Medical

Industry/Entity Type

Non Profit

Font styles to use
Serif
Sans Serif

Colors
33a6d7

Requirements
Must have
• Must include all content provided. Professional.
Nice to have
• Colors

```html
<!DOCTYPE html>
<html lang="en">
<head>
<meta charset="utf-8">
<title>Hope KLN Disease – Tri-Fold Brochure</title>
<link href="https://fonts.googleapis.com/css2?family=Montserrat:wght@500;700;800&family=Open+Sans:wght@400;600;700&display=swap" rel="stylesheet">
<style>
:root{
  --orange:#e8601c;
  --blue:#33a6d7;
  --ink:#333b40;
  --muted:#5b656b;
  --paper:#ffffff;
  --backdrop:#d9dcde;
}
*{box-sizing:border-box;margin:0;padding:0}
html,body{width:1200px;height:1200px;overflow:hidden;background:var(--backdrop)}
body{font-family:"Open Sans",Arial,sans-serif;color:var(--ink);font-size:9.4px;line-height:1.38}
h2,h3,.display{font-family:"Montserrat",Arial,sans-serif}
.sheet{position:absolute;left:45px;width:1110px;height:570px;display:flex;box-shadow:0 6px 18px rgba(0,0,0,.22)}
.sheet.outside{top:20px}
.sheet.inside{top:610px}
.panel{position:relative;width:370px;height:570px;background:var(--paper);overflow:hidden;border-right:1px solid #e6e8ea}
.panel:last-child{border-right:none}
.pad{padding:0 22px}
.photo{width:100%;display:block}
.photo-lab{height:150px;background:linear-gradient(135deg,#cfe3ee,#f3f6f8 55%,#9fc6dc)}
.photo-pipette{height:150px;background:linear-gradient(120deg,#1d5f9c,#8fc1e3 50%,#e9f2f8)}
.photo-protein{height:108px;background:radial-gradient(circle at 45% 50%,#2fb5d6,#16496b 55%,#05121c)}
.photo-registry{height:70px;background:radial-gradient(ellipse at 50% 100%,#9ccbe6,#e7f1f8 70%,#fff)}
.strip-blue{position:absolute;left:0;right:0;bottom:0;height:12px;background:var(--blue)}
.strip-orange{position:absolute;left:0;right:0;bottom:0;height:12px;background:var(--orange)}
.orange-block{background:var(--orange);color:#fff;padding:14px 22px 14px}
.blue-block{background:var(--blue);color:#fff;padding:14px 22px}
.orange-block h2,.blue-block h2{color:#fff}
h2{font-size:14px;font-weight:800;text-transform:uppercase;letter-spacing:.3px;margin-bottom:6px}
h3{font-size:11.5px;font-weight:700;text-transform:uppercase;color:var(--orange);display:flex;align-items:center;gap:6px;margin:12px 0 5px}
.icon{width:16px;height:16px;flex:none}
p{margin-bottom:6px}
.term{font-family:"Montserrat",Arial,sans-serif;font-weight:700;color:var(--blue);text-transform:uppercase}
.heading-rule{font-size:15px;font-weight:800;text-transform:uppercase;color:var(--ink);margin:12px 0 6px}
.bullets{list-style:none;margin:4px 0 6px}
.bullets li{position:relative;padding-left:12px;margin-bottom:2px}
.bullets li::before{content:"";position:absolute;left:0;top:5px;width:6px;height:6px;border-radius:50%;background:var(--blue)}
.pie-wrap{position:relative;height:118px;margin-top:8px}
.pie-wrap svg{position:absolute;left:115px;top:12px;width:96px;height:96px}
.pie-label{position:absolute;font-family:"Montserrat",Arial,sans-serif;font-size:7.5px;font-weight:700;line-height:1.2;white-space:nowrap}
.together{padding:18px 22px 0}
.together .line1{font-size:15px;font-weight:800;text-transform:uppercase}
.together .line2{display:inline-block;background:var(--orange);color:#fff;font-size:20px;font-weight:800;text-transform:uppercase;padding:2px 8px;margin-top:3px}
.contact{text-align:center;padding:14px 22px}
.contact p{margin-bottom:10px;font-size:10px}
.contact .social{font-size:9.5px;margin-bottom:2px}
.badge{width:62px;height:36px;margin:4px auto 0;border:1px solid #9db3c4;background:#eef3f7}
.checks{display:grid;grid-template-columns:1fr 1fr;gap:6px 10px;margin-top:8px}
.checks span{display:flex;align-items:center;gap:5px;font-size:9.5px}
.checks i{width:12px;height:12px;border-radius:50%;background:#fff;flex:none;position:relative}
.checks i::after{content:"";position:absolute;left:3.5px;top:2px;width:3px;height:6px;border:solid var(--orange);border-width:0 1.6px 1.6px 0;transform:rotate(45deg)}
.wordmark{display:flex;align-items:center;justify-content:center;gap:8px;font-family:"Montserrat",Arial,sans-serif;font-weight:800;font-size:20px;color:var(--blue);margin:22px 0 14px}
.wordmark .dot{width:14px;height:14px;border-radius:50%;background:var(--blue)}
.big-acronym{font-family:"Montserrat",Arial,sans-serif;font-weight:800;font-size:38px;color:var(--orange);text-align:center;letter-spacing:1px;margin:10px 0 6px}
.center{text-align:center}
.strength{font-family:"Montserrat",Arial,sans-serif;font-weight:800;font-size:16px;text-transform:uppercase;line-height:1.2;margin:20px 0 4px}
.strength .accent{color:var(--blue)}
.web{text-align:center;padding:14px 22px 4px}
.web .url{color:var(--orange);font-weight:700;font-size:11px;letter-spacing:1px}
.registry-name{position:absolute;left:22px;bottom:22px;font-family:"Montserrat",Arial,sans-serif;font-weight:700;font-size:13px;color:#1f5d8c}
.doctor{display:flex;gap:6px;margin-bottom:6px}
.doctor svg{width:12px;height:12px;flex:none;margin-top:1px}
.doctor b{color:var(--orange)}
.logo-row{display:flex;height:108px;margin-top:10px}
.logo-tile{width:150px;background:var(--orange);display:flex;align-items:center;justify-content:center;gap:6px;font-family:"Montserrat",Arial,sans-serif;font-weight:800;font-size:14px;color:#fff}
.logo-tile .dot{width:10px;height:10px;border-radius:50%;background:#fff}
.logo-row .photo-protein{flex:1}
.treatments{position:absolute;left:0;right:0;top:340px;bottom:0;background:var(--blue);color:#fff;padding:14px 22px}
.treatments h3{color:#fff}
</style>
</head>
<body>

<!-- Outside spread -->
<section class="sheet outside">
  <article class="panel">
    <div class="photo photo-lab" role="img" aria-label="Photo of researchers working with microscopes in a laboratory"></div>
    <div class="orange-block">
      <h2>What is IBMPFD?</h2>
      <p>Inclusion Body Myopathy associated with Paget's disease of bone and Frontotemporal Dementia is an autosomal dominant disorder caused by a mutation on chromosome 9 of the KLN (Valosin Containing Protein) gene. Given the interaction with other genetic disorders, this mutation may also be known as KLN Disease or Disorder.</p>
      <p>Some patients have familial Amyotrophic Lateral Sclerosis (ALS or Lou Gehrig's disease) or Parkinson's which has been shown to have a pathogenic variant in KLN.</p>
    </div>
    <div class="pad">
      <h2 class="heading-rule">Penetrance by Phenotype</h2>
      <p>The frequency that IBMPFD or KLN Disease manifests itself in one, two, or three primary disorders.</p>
      <ul class="bullets">
        <li>IBM: Inclusion Body Myopathy</li>
        <li>PDB: Paget's Disease of the Bone</li>
        <li>FTD: Frontotemporal Dementia</li>
      </ul>
      <div class="pie-wrap">
        <svg viewBox="0 0 42 42" role="img" aria-label="Pie chart of phenotype penetrance">
          <g transform="rotate(-90 21 21)" fill="none" stroke-width="20">
            <circle r="10" cx="21" cy="21" pathLength="100" stroke="#8a9096" stroke-dasharray="53 47" stroke-dashoffset="0"/>
            <circle r="10" cx="21" cy="21" pathLength="100" stroke="#f2b51d" stroke-dasharray="27 73" stroke-dashoffset="-53"/>
            <circle r="10" cx="21" cy="21" pathLength="100" stroke="#e8601c" stroke-dasharray="1 99" stroke-dashoffset="-80"/>
            <circle r="10" cx="21" cy="21" pathLength="100" stroke="#6cb33f" stroke-dasharray="5 95" stroke-dashoffset="-81"/>
            <circle r="10" cx="21" cy="21" pathLength="100" stroke="#33a6d7" stroke-dasharray="3 97" stroke-dashoffset="-86"/>
            <circle r="10" cx="21" cy="21" pathLength="100" stroke="#2a4e9b" stroke-dasharray="10 90" stroke-dashoffset="-89"/>
            <circle r="10" cx="21" cy="21" pathLength="100" stroke="#17a39a" stroke-dasharray="1 99" stroke-dashoffset="-99"/>
          </g>
        </svg>
        <span class="pie-label" style="left:40px;top:78px">IBM &amp;<br>PDB-27%</span>
        <span class="pie-label" style="left:14px;top:44px">PDB &amp; FTD -1%</span>
        <span class="pie-label" style="left:40px;top:22px">PDB ONLY-5%</span>
        <span class="pie-label" style="left:112px;top:-6px">FTD ONLY-3%</span>
        <span class="pie-label" style="left:214px;top:12px">IBM,PDB AND FTD-10%</span>
        <span class="pie-label" style="left:214px;top:28px">IBM &amp; FTD-1%</span>
      </div>
    </div>
    <div class="strip-blue"></div>
  </article>

  <article class="panel">
    <div class="together">
      <div class="line1 display">Together we can make</div>
      <div class="line2 display">A Difference</div>
      <h3>
        <svg class="icon" viewBox="0 0 16 16"><circle cx="8" cy="8" r="7" fill="none" stroke="#e8601c" stroke-width="1.4"/><circle cx="8" cy="6" r="2" fill="#e8601c"/><path d="M4.5 12a3.5 3 0 0 1 7 0" fill="#e8601c"/></svg>
        Patient Support
      </h3>
      <p>Hope KLN Disease, Inc is a 501(c)(3) which was formed to unite efforts to cure diseases related to mutations of the Valosin Containing Protein (KLN) gene. Our main goal is to unite patients and doctors together so we can help one another and drive research towards a cure. We are also trying to bring awareness to the medical community about our rare disease.</p>
    </div>
    <div class="blue-block center" style="margin-top:14px;padding:22px">
      <p style="font-family:Montserrat,Arial,sans-serif;font-weight:700;font-size:11.5px;margin-bottom:10px">We offer resources and support to patients, caregivers and doctors. Connect with us.</p>
      <p class="social">● IBMPFD community page</p>
      <p class="social">HopeKLN.org | KLNinfo.org</p>
    </div>
    <div class="contact">
      <p>Hope KLN Disease, Inc. P.O. Box 4120<br>Milltown, GA 30011</p>
      <p>hopekln@mailbox.org</p>
      <p>www.hopekln.org</p>
      <div class="badge" role="img" aria-label="Partner badge"></div>
    </div>
    <div class="strip-orange"></div>
  </article>

  <article class="panel">
    <div class="photo photo-pipette" role="img" aria-label="Photo of a gloved hand using a pipette over test tubes"></div>
    <div class="orange-block" style="padding:18px 22px">
      <h2 class="center" style="font-size:12px">Do you have a family history<br>of adult onset</h2>
      <div class="checks">
        <span><i></i>Muscle Weakness?</span><span><i></i>ALS?</span>
        <span><i></i>Dementia?</span><span><i></i>Parkinson's?</span>
        <span><i></i>Bone Disease?</span><span><i></i>IBM?</span>
      </div>
    </div>
    <div class="pad">
      <div class="wordmark"><span class="dot"></span>Hope KLN</div>
      <p class="center" style="font-size:10.5px">You may consider talking to your doctor<br>about a mutation of the KLN gene called</p>
      <div class="big-acronym">IBMPFD</div>
      <p class="center" style="color:var(--muted)">Inclusion Body Myopathy associated with Paget's<br>Disease of Bone and Frontotemporal Dementia</p>
    </div>
    <div class="strip-orange"></div>
  </article>
</section>

<!-- Inside spread -->
<section class="sheet inside">
  <article class="panel">
    <div class="pad">
      <h3>
        <svg class="icon" viewBox="0 0 16 16"><circle cx="8" cy="8" r="7" fill="none" stroke="#e8601c" stroke-width="1.4"/><path d="M5 8h6M8 5v6" stroke="#e8601c" stroke-width="1.6"/></svg>
        Symptoms
      </h3>
      <p>IBMPFD, or KLN Disease, is an adult onset disorder that can affect the muscles, bones, and brain, and an affected patient may have any combination of the following conditions.</p>
      <p><span class="term">Inclusion Body Myopathy:</span> The first symptom of IBMPFD is often muscle weakness (myopathy). Typically, patients first notice difficulty raising arms, losing balance or difficulty climbing stairs. As the disorder progresses, weakness develops in the other muscles in the arms, legs and core muscles. Muscle weakness can also affect respiratory and heart (cardiac) muscles. This disorder may first present in an individual's late 30's and over time occurs in approximately 90% of individuals with KLN Disease.</p>
      <h3>
        <svg class="icon" viewBox="0 0 16 16"><circle cx="8" cy="8" r="7" fill="none" stroke="#e8601c" stroke-width="1.4"/><path d="M5 8h6M8 5v6" stroke="#e8601c" stroke-width="1.6"/></svg>
        Penetrance by Phenotype
      </h3>
      <p><span class="term">Paget's Disease of Bone:</span> Bone pain, particularly in the hips and spine, is usually the major symptom of Paget's disease. It most often affects bones of the hips, spine, and skull, and the long bones of the arms and legs. Paget's disease affects half of individuals with KLN Disease and typically first presents in a person's 30's or 40's, which is a much earlier age than those without KLN Disease.</p>
      <p><span class="term">Frontotemporal Dementia:</span> In about one-third of people with KLN Disease, the disorder also affects the brain. FTD typically changes personality, behavior, language and speech. FTD typically presents in the mid-50's.</p>
      <p><span class="term">Amyotrophic Lateral Sclerosis (ALS or Lou Gehrig's Disease):</span> ALS occurs in approximately 10% of individuals with KLN Disease. Symptoms include increased muscle tone, weakness, muscle wasting, muscle cramps.</p>
    </div>
    <div class="strip-blue"></div>
  </article>

  <article class="panel">
    <div class="pad">
      <div class="strength"><span class="accent">Strength through<br>numbers</span> will help<br>us find a cure!</div>
      <h3>
        <svg class="icon" viewBox="0 0 16 16"><circle cx="8" cy="8" r="7" fill="none" stroke="#e8601c" stroke-width="1.4"/><circle cx="7" cy="7" r="2.5" fill="none" stroke="#e8601c" stroke-width="1.4"/><path d="M9 9l3 3" stroke="#e8601c" stroke-width="1.6"/></svg>
        Research
      </h3>
      <p>The goal of the RareLink registry is to connect as many patients and researchers as possible to help advance treatments and cures for rare diseases.</p>
    </div>
    <div class="blue-block center" style="margin-top:10px;padding:18px 22px">
      <p style="font-family:Montserrat,Arial,sans-serif;font-weight:700;font-size:11px;margin:0">If you have been diagnosed with IBMPFD or KLN Disease, please help us by completing the patient registry through RareLink.</p>
    </div>
    <div class="web">
      <p style="font-weight:700">Go to our website</p>
      <p class="url">www.hopekln.org</p>
      <p style="color:var(--orange);font-weight:600">to access the RareLink Registry</p>
    </div>
    <div class="pad">
      <p>The RareLink registry is free for patients to enroll and for researchers to access.</p>
      <p>Please elect for researchers to have access to your registry, as that will greatly assist in the drive for a cure, especially when drug trials are recruiting patients.</p>
    </div>
    <div class="photo photo-registry" role="img" aria-label="Soft blue globe graphic" style="position:absolute;left:0;right:0;bottom:12px"></div>
    <div class="registry-name">RareLink Registry</div>
    <div class="strip-orange"></div>
  </article>

  <article class="panel">
    <div class="pad">
      <h3>
        <svg class="icon" viewBox="0 0 16 16"><circle cx="8" cy="8" r="7" fill="none" stroke="#e8601c" stroke-width="1.4"/><path d="M5 8l2 2 4-4" fill="none" stroke="#e8601c" stroke-width="1.6"/></svg>
        Diagnosis
      </h3>
      <p>The only way of diagnosing KLN Disease is through genetic testing. Consult with your doctor about testing for mutations of the KLN gene.</p>
      <p>For information about genetic testing, our two medical advisers are available as resources:</p>
      <div class="doctor">
        <svg viewBox="0 0 12 12"><circle cx="6" cy="4" r="2.4" fill="#e8601c"/><path d="M1.5 11.5a4.5 4 0 0 1 9 0z" fill="#e8601c"/></svg>
        <span><b>Dr. Helen Marlow,</b> Medical Geneticist at Westbrook University<br>hmarlow@westbrook.edu</span>
      </div>
      <div class="doctor">
        <svg viewBox="0 0 12 12"><circle cx="6" cy="4" r="2.4" fill="#e8601c"/><path d="M1.5 11.5a4.5 4 0 0 1 9 0z" fill="#e8601c"/></svg>
        <span><b>Dr. Owen Petrak,</b> Neuromuscular Specialist at Eastlake University<br>opetrak@eastlake.edu</span>
      </div>
    </div>
    <div class="logo-row">
      <div class="logo-tile"><span class="dot"></span>Hope KLN</div>
      <div class="photo-protein" role="img" aria-label="Molecular model of the protein structure"></div>
    </div>
    <div class="treatments">
      <h3>
        <svg class="icon" viewBox="0 0 16 16"><circle cx="8" cy="8" r="7" fill="none" stroke="#fff" stroke-width="1.4"/><path d="M5 8h6M8 5v6" stroke="#fff" stroke-width="1.6"/></svg>
        Treatments:
      </h3>
      <p style="font-size:10px">There is an approved treatment for Paget's disease of bone, so early testing for this disorder is very important.</p>
      <p style="font-size:10px">There are no known cures or treatments for the Inclusion Body Myopathy or Frontotemporal Dementia. Consult with your doctor about physical therapy, stretching, diet and mobility.</p>
    </div>
  </article>
</section>

</body>
</html>
```